Help designing a web admin portal for cloud access control company

Hello, we need help to design our web admin portal for our cloud based access control product called halcyon gatekeep. Please see the attached admin portal wireframe. this is not absolute so we are open to UX / UI suggestions. This web admin portal will allow a admin at a small to medium sized business add new employees to their access control system and grant different access.
Updates

Project Deadline Extended
Reason: Waiting in a couple designs for people that said they would send something in

Target Market(s)

B2B

Industry/Entity Type

It Company

Font styles to use
Sans Serif

Colors
3277b5

Requirements
Must have
• Very simple and clean design. we like clean fonts like Oswald extra light. Please see an image of the wining app designs to see what the color and styling should look like

```html
<!DOCTYPE html>
<html lang="en">
<head>
<meta charset="utf-8">
<title>Halcyon Gatekeep – Open/Close Times</title>
<link rel="stylesheet" href="https://fonts.googleapis.com/css2?family=Lato:wght@400;700&display=swap">
<style>
:root{
  --sidebar:#1f2a35;
  --topbar:#1c2024;
  --band:#24282c;
  --page:#eceff1;
  --card:#ffffff;
  --accent:#1b9ad6;
  --accent-bright:#27b4f0;
  --text-light:#ffffff;
  --text-muted:#aeb6bd;
  --text-dark:#222;
  --cell:#f6f6f6;
  --line:#e2e2e2;
  --open:#b3e9c4;
  --alert:#d9453b;
}
*{box-sizing:border-box;margin:0;padding:0}
html,body{width:1200px;height:1029px;overflow:hidden}
body{font-family:"Lato",sans-serif;background:var(--page);position:relative}
.sidebar{position:absolute;left:0;top:0;width:175px;height:975px;background:var(--sidebar)}
.brand{position:absolute;left:17px;top:20px}
.brand-mark{width:30px;height:30px;background:var(--text-light);display:block}
.brand-name{position:absolute;left:0;top:56px;white-space:nowrap;color:var(--text-light);font-size:11px;font-weight:700;letter-spacing:.3px}
.nav{position:absolute;top:111px;left:0;width:175px;list-style:none}
.nav li{height:34.3px;display:flex;align-items:center;padding-left:16px;color:var(--text-light);font-size:12.5px;position:relative}
.nav li svg{width:12px;height:12px;margin-right:13px;fill:var(--accent)}
.nav li .chev{position:absolute;right:12px;top:50%;width:5px;height:5px;border-top:1.2px solid var(--text-muted);border-right:1.2px solid var(--text-muted);transform:translateY(-50%) rotate(45deg)}
.nav li.active{background:var(--accent)}
.nav li.active::after{content:"";position:absolute;right:0;top:0;width:4px;height:100%;background:var(--accent-bright)}
.nav li.active svg{fill:var(--text-light)}
.nav li.active .chev{border-color:var(--text-light)}
.count{position:absolute;right:30px;top:50%;transform:translateY(-50%);width:15px;height:15px;border-radius:50%;background:var(--alert);font-size:9.5px;text-align:center;line-height:15px}
.topbar{position:absolute;left:175px;top:0;width:1025px;height:49px;background:var(--topbar);border-bottom:1px solid #2c3136}
.topbar-title{position:absolute;left:24px;top:16px;color:var(--text-light);font-weight:700;font-size:14px}
.doors{position:absolute;left:184px;top:0;display:flex}
.door{width:77px;height:48px;border-left:1px solid #30353a;display:flex;flex-direction:column;align-items:center;justify-content:center;color:var(--text-muted);font-size:9px;gap:4px}
.door:last-child{border-right:1px solid #30353a}
.door svg{width:11px;height:14px;fill:#c9ced3}
.search{position:absolute;left:676px;top:11px;width:161px;height:26px;border-radius:13px;background:#33383d;color:#d7dbdf;font-size:12px;line-height:26px;padding-left:12px}
.search svg{position:absolute;right:10px;top:8px;width:10px;height:10px}
.bell{position:absolute;left:876px;top:16px;width:16px;height:18px}
.bell-count{position:absolute;left:884px;top:10px;width:12px;height:12px;border-radius:50%;background:var(--alert);color:#fff;font-size:8px;text-align:center;line-height:12px}
.avatar{position:absolute;left:913px;top:9px;width:29px;height:29px;border-radius:50%;background:linear-gradient(135deg,#8a5b45,#d4b49a)}
.online{position:absolute;left:935px;top:31px;width:8px;height:8px;border-radius:50%;background:#3cc46a;border:1.5px solid var(--topbar)}
.logout{position:absolute;left:961px;top:17px;color:var(--text-light);font-size:12px;display:flex;align-items:center;gap:3px}
.logout svg{width:9px;height:9px}
.band{position:absolute;left:175px;top:49px;width:1025px;height:61px;background:var(--band)}
.band h1{position:absolute;left:22px;top:17px;color:var(--text-light);font-size:21px;font-weight:700}
.card{position:absolute;left:200px;top:141px;width:975px;height:800px;background:var(--card);border-radius:2px}
.card-head{height:42px;border-bottom:1px solid #e8eaec;padding-left:22px;line-height:42px;font-size:15.5px;color:#444}
.filter{position:absolute;left:23px;top:59px;width:188px;height:32px;border:1px solid #dfe2e5;border-radius:2px;font-size:11.5px;color:#555;line-height:30px;padding-left:12px}
.filter::after{content:"";position:absolute;right:11px;top:13px;border:4px solid transparent;border-top:5px solid #555}
.schedule{position:absolute;left:23px;top:107px;border-collapse:collapse;table-layout:fixed;width:929px;font-size:11.5px}
.schedule th{height:29px;background:#fff;border:1px solid var(--line);font-weight:700;color:var(--text-dark);width:123.7px}
.schedule th.time-col{width:63px}
.schedule td{height:26.6px;border:1px solid var(--line);background:var(--cell)}
.schedule td.hour{background:#fff;text-align:right;padding-right:8px;color:var(--text-dark)}
.schedule td.on{background:var(--open);border-color:#a6dcb7}
.footer{position:absolute;left:0;top:975px;width:1200px;height:54px;background:var(--topbar);color:#b6bcc2;font-size:12.5px;text-align:center;line-height:54px}
</style>
</head>
<body>
<aside class="sidebar">
  <div class="brand"><span class="brand-mark"></span><span class="brand-name">HALCYON GATEKEEP</span></div>
  <ul class="nav">
    <li><svg viewBox="0 0 12 12"><path d="M6 1 0 6h2v5h3V8h2v3h3V6h2z"/></svg>Home<span class="chev"></span></li>
    <li><svg viewBox="0 0 12 12"><rect x="0" y="1" width="5" height="4"/><rect x="7" y="1" width="5" height="4"/><rect x="0" y="7" width="5" height="4"/><rect x="7" y="7" width="5" height="4"/></svg>Dashboard<span class="chev"></span></li>
    <li><svg viewBox="0 0 12 12"><rect y="2" width="12" height="1.5"/><rect y="5.5" width="12" height="1.5"/><rect y="9" width="12" height="1.5"/><rect x="7" y="1" width="2" height="3.5"/><rect x="3" y="4.5" width="2" height="3.5"/><rect x="8" y="8" width="2" height="3.5"/></svg>Controller<span class="chev"></span></li>
    <li><svg viewBox="0 0 12 12"><path d="M5 3v2H0v2h5v2l3-3zM8 1h4v10H8V9.5h2.5v-7H8z"/></svg>Doors<span class="chev"></span></li>
    <li><svg viewBox="0 0 12 12"><circle cx="6" cy="3.3" r="2.8"/><path d="M1 12c0-4 2-5.5 5-5.5s5 1.5 5 5.5z"/></svg>Employees<span class="chev"></span></li>
    <li class="active"><svg viewBox="0 0 12 12"><path d="M6 0a6 6 0 1 0 0 12A6 6 0 0 0 6 0zm0 2a4 4 0 1 1 0 8 4 4 0 0 1 0-8zM5.3 3.2v3.3h2.8V5.3H6.6V3.2z"/></svg>Open/Close Times<span class="chev"></span></li>
    <li><svg viewBox="0 0 12 12"><path d="M4 1h4l1 2h3v8H0V3h3z"/><circle cx="6" cy="6.8" r="2" fill="#1f2a35"/></svg>Cameras<span class="chev"></span></li>
    <li><svg viewBox="0 0 12 12"><path d="M0 2h12v10H0zM1 4.5v6.5h10V4.5zM2.5 0h1.5v3H2.5zM8 0h1.5v3H8z"/><rect x="2.5" y="6" width="7" height="1"/><rect x="2.5" y="8.5" width="7" height="1"/></svg>Time Card<span class="chev"></span></li>
    <li><svg viewBox="0 0 12 12"><path d="M2 0h5l3 3v9H2z"/></svg>Reports<span class="chev"></span></li>
    <li><svg viewBox="0 0 12 12"><path d="M5 0h2l.3 1.7 1.4.6 1.4-1 1.4 1.4-1 1.4.6 1.4L12 5v2l-1.7.3-.6 1.4 1 1.4-1.4 1.4-1.4-1-1.4.6L7 12H5l-.3-1.7-1.4-.6-1.4 1L.5 9.3l1-1.4-.6-1.4L0 7V5l1.7-.3.6-1.4-1-1.4L2.7.5l1.4 1 1.4-.6z"/><circle cx="6" cy="6" r="1.8" fill="#1f2a35"/></svg>Settings<span class="count">2</span><span class="chev"></span></li>
  </ul>
</aside>

<header class="topbar">
  <div class="topbar-title">Manual Door Opening</div>
  <nav class="doors">
    <div class="door"><svg viewBox="0 0 11 14"><path d="M0 1 8 0v14L0 13z"/><rect x="9" y="1" width="2" height="12"/></svg>Main Door</div>
    <div class="door"><svg viewBox="0 0 11 14"><path d="M0 1 8 0v14L0 13z"/><rect x="9" y="1" width="2" height="12"/></svg>Back Door</div>
    <div class="door"><svg viewBox="0 0 11 14"><path d="M0 1 8 0v14L0 13z"/><rect x="9" y="1" width="2" height="12"/></svg>Exec Office</div>
    <div class="door"><svg viewBox="0 0 11 14"><path d="M0 1 8 0v14L0 13z"/><rect x="9" y="1" width="2" height="12"/></svg>Storage Room</div>
  </nav>
  <div class="search">Search<svg viewBox="0 0 10 10"><circle cx="4" cy="4" r="3" fill="none" stroke="#fff" stroke-width="1.6"/><path d="M6.2 6.2 9.3 9.3" stroke="#fff" stroke-width="1.8"/></svg></div>
  <svg class="bell" viewBox="0 0 16 18"><path d="M8 1.5c-3 0-5 2.2-5 5v4.5L1.5 13h13L13 11V6.5c0-2.8-2-5-5-5zM6 15a2 2 0 0 0 4 0" fill="none" stroke="#fff" stroke-width="1.4"/></svg>
  <span class="bell-count">2</span>
  <div class="avatar" role="img" aria-label="Signed-in administrator profile photo"></div>
  <span class="online"></span>
  <div class="logout"><svg viewBox="0 0 9 9"><path d="M0 0h4v1.5H1.5v6H4V9H0zM5 2l3 2.5L5 7V5.3H2.5V3.7H5z" fill="#fff"/></svg>Logout</div>
</header>

<div class="band"><h1>Open/Close Times</h1></div>

<main class="card">
  <div class="card-head">Open/Close Times</div>
  <div class="filter">Department: All Employees</div>
  <table class="schedule">
    <thead><tr><th class="time-col"></th><th>Monday</th><th>Tuesday</th><th>Wednesday</th><th>Thursday</th><th>Friday</th><th>Saturday</th><th>Sunday</th></tr></thead>
    <tbody>
      <tr><td class="hour">12am</td><td></td><td></td><td></td><td></td><td></td><td></td><td></td></tr>
      <tr><td class="hour">1am</td><td></td><td></td><td></td><td></td><td></td><td></td><td></td></tr>
      <tr><td class="hour">2am</td><td></td><td></td><td></td><td></td><td></td><td></td><td></td></tr>
      <tr><td class="hour">3am</td><td></td><td></td><td></td><td></td><td></td><td></td><td></td></tr>
      <tr><td class="hour">4am</td><td></td><td></td><td></td><td></td><td></td><td></td><td></td></tr>
      <tr><td class="hour">5am</td><td></td><td></td><td></td><td></td><td></td><td></td><td></td></tr>
      <tr><td class="hour">6am</td><td></td><td></td><td></td><td></td><td></td><td></td><td></td></tr>
      <tr><td class="hour">7am</td><td class="on"></td><td class="on"></td><td class="on"></td><td class="on"></td><td class="on"></td><td></td><td></td></tr>
      <tr><td class="hour">8am</td><td class="on"></td><td class="on"></td><td class="on"></td><td class="on"></td><td class="on"></td><td></td><td></td></tr>
      <tr><td class="hour">9am</td><td class="on"></td><td class="on"></td><td class="on"></td><td class="on"></td><td class="on"></td><td class="on"></td><td class="on"></td></tr>
      <tr><td class="hour">10am</td><td class="on"></td><td class="on"></td><td class="on"></td><td class="on"></td><td class="on"></td><td class="on"></td><td class="on"></td></tr>
      <tr><td class="hour">11am</td><td class="on"></td><td class="on"></td><td class="on"></td><td class="on"></td><td class="on"></td><td class="on"></td><td class="on"></td></tr>
      <tr><td class="hour">12pm</td><td class="on"></td><td class="on"></td><td class="on"></td><td class="on"></td><td class="on"></td><td class="on"></td><td class="on"></td></tr>
      <tr><td class="hour">1pm</td><td class="on"></td><td class="on"></td><td class="on"></td><td class="on"></td><td class="on"></td><td class="on"></td><td class="on"></td></tr>
      <tr><td class="hour">2pm</td><td class="on"></td><td class="on"></td><td class="on"></td><td class="on"></td><td class="on"></td><td class="on"></td><td class="on"></td></tr>
      <tr><td class="hour">3pm</td><td class="on"></td><td class="on"></td><td class="on"></td><td class="on"></td><td class="on"></td><td class="on"></td><td class="on"></td></tr>
      <tr><td class="hour">4pm</td><td class="on"></td><td class="on"></td><td class="on"></td><td class="on"></td><td class="on"></td><td class="on"></td><td class="on"></td></tr>
      <tr><td class="hour">5pm</td><td class="on"></td><td class="on"></td><td class="on"></td><td class="on"></td><td class="on"></td><td></td><td></td></tr>
      <tr><td class="hour">6pm</td><td class="on"></td><td class="on"></td><td class="on"></td><td class="on"></td><td class="on"></td><td></td><td></td></tr>
      <tr><td class="hour">7pm</td><td></td><td></td><td></td><td></td><td></td><td></td><td></td></tr>
      <tr><td class="hour">8pm</td><td></td><td></td><td></td><td></td><td></td><td></td><td></td></tr>
      <tr><td class="hour">9pm</td><td></td><td></td><td></td><td></td><td></td><td></td><td></td></tr>
      <tr><td class="hour">10pm</td><td></td><td></td><td></td><td></td><td></td><td></td><td></td></tr>
      <tr><td class="hour">11pm</td><td></td><td></td><td></td><td></td><td></td><td></td><td></td></tr>
    </tbody>
  </table>
</main>

<footer class="footer">© 2016 Halcyon Gatekeep</footer>
</body>
</html>
```